Pest Control Company needs business card!

Hi there, we need a business card designed for our new Pest Control Company. Ideally this card will be simple, yet feel elegant and high end. We want to use the colours Orange, Black and White. Please see our attached logo for the exact colours.

Business card details:

Phone - 0461 275 804
Name - Gavin Holloway
Email - Info@steadfastverminguard.com.au

We would also like to include the following list with dot points:

SERVICES / INSPECTIONS

Termites, Wood Borers, Ants, Cockroaches, Spiders, Fleas, Mice, Rats, Bed Bugs, & More!

```html
<!DOCTYPE html>
<html lang="en">
<head>
<meta charset="utf-8">
<title>Steadfast Vermin Guard – Business Card</title>
<link rel="stylesheet" href="https://fonts.googleapis.com/css2?family=Montserrat:wght@800;900&family=Lato:wght@400;700&display=swap">
<style>
  :root {
    --yellow: #ffdf1c;
    --ink: #1b1b1b;
    --red: #e8262d;
    --orange: #f07a1e;
    --white: #ffffff;
    --stage: #d9d9d9;
    --mascot: #2a2a2a;
  }
  * { box-sizing: border-box; margin: 0; padding: 0; }
  html, body { width: 1200px; height: 960px; overflow: hidden; }
  body {
    background: var(--stage);
    display: flex;
    flex-direction: column;
    align-items: center;
    justify-content: center;
    gap: 36px;
    font-family: "Lato", sans-serif;
    color: var(--ink);
  }
  .card {
    position: relative;
    width: 720px;
    height: 430px;
    overflow: hidden;
    box-shadow: 0 10px 28px rgba(0,0,0,.22);
  }

  .brand-name {
    font-family: "Montserrat", sans-serif;
    font-weight: 900;
    color: var(--ink);
    text-transform: uppercase;
    line-height: .95;
    letter-spacing: -1px;
  }
  .mascot {
    background: radial-gradient(circle closest-side at 50% 50%, var(--mascot) 0 78%, rgba(42,42,42,.2) 92%, rgba(42,42,42,0) 100%);
  }

  /* Front */
  .card--front { background: var(--yellow); }
  .front-brand {
    position: absolute;
    left: 150px; top: 62px;
    display: flex; align-items: center; gap: 24px;
  }
  .front-brand .brand-name { font-size: 48px; }
  .front-brand .mascot { width: 190px; height: 190px; flex: none; }
  .services {
    position: absolute;
    left: 0; right: 0; bottom: 58px;
    text-align: center;
    font-size: 21px;
    line-height: 1.55;
  }
  .services .dot { color: var(--red); font-weight: 700; margin: 0 6px; }

  /* Back */
  .card--back { background: var(--white); }
  .back-brand {
    position: absolute;
    left: 44px; top: 58px;
  }
  .back-brand .brand-name { font-size: 46px; }
  .card--back .mascot {
    position: absolute;
    right: 28px; top: 24px;
    width: 300px; height: 300px;
  }
  .person { position: absolute; left: 92px; top: 232px; }
  .person-name {
    font-family: "Montserrat", sans-serif;
    font-weight: 800;
    font-size: 26px;
    text-transform: uppercase;
    white-space: nowrap;
  }
  .person-role { font-size: 21px; margin-top: 2px; }
  .contacts {
    position: absolute;
    left: 92px; top: 318px;
    list-style: none;
    font-size: 20px;
    line-height: 1.45;
  }
  .contacts li { display: flex; align-items: center; gap: 10px; white-space: nowrap; }
  .contacts svg { width: 16px; height: 16px; fill: var(--orange); flex: none; }
  .edge-tab {
    position: absolute;
    left: 0; top: 300px;
    width: 18px; height: 56px;
    background: var(--red);
  }
</style>
</head>
<body>

<section class="card card--front" aria-label="Card front">
  <div class="front-brand">
    <p class="brand-name">Steadfast<br>Vermin<br>Guard</p>
    <div class="mascot" role="img" aria-label="Cartoon illustration of a startled black bug with a red exclamation mark"></div>
  </div>
  <p class="services">
    <span class="dot">•</span>Termites<span class="dot">•</span>Wood Borers<span class="dot">•</span>Ants<span class="dot">•</span>Cockroaches<span class="dot">•</span>Spiders<br>
    <span class="dot">•</span>Fleas<span class="dot">•</span>Mice<span class="dot">•</span>Rats<span class="dot">•</span>Bed Bugs &amp;<span class="dot">•</span>More!
  </p>
</section>

<section class="card card--back" aria-label="Card back">
  <div class="back-brand">
    <p class="brand-name">Steadfast<br>Vermin<br>Guard</p>
  </div>
  <div class="mascot" role="img" aria-label="Large cartoon illustration of a startled black bug with a red exclamation mark"></div>
  <span class="edge-tab"></span>
  <div class="person">
    <p class="person-name">Gavin Holloway</p>
    <p class="person-role">Founder &amp; CEO</p>
  </div>
  <ul class="contacts">
    <li>
      <svg viewBox="0 0 16 16" aria-hidden="true"><path d="M3.6 1.5l2.2 2.6-1.3 1.6c.9 2 2.4 3.6 4.4 4.6l1.6-1.3 2.6 2.2-1.5 2.3C6.6 13.2 2.8 9.4 1.3 3z"/></svg>
      0461 275 804
    </li>
    <li>
      <svg viewBox="0 0 16 16" aria-hidden="true"><path d="M1 3h14v10H1z M2 4l6 5 6-5" stroke="#fff" stroke-width="1"/></svg>
      Info@steadfastverminguard.com.au
    </li>
    <li>
      <svg viewBox="0 0 16 16" aria-hidden="true"><circle cx="8" cy="8" r="7"/><path d="M1 8h14M8 1c-3 4-3 10 0 14M8 1c3 4 3 10 0 14" stroke="#fff" stroke-width="1" fill="none"/></svg>
      www.steadfastverminguard.com.au
    </li>
  </ul>
</section>

</body>
</html>
```